Business card to promote business guidance

I need a card design to give to all my customers advertising a way to build a business exactly like the one they just bought from. I have an online store and will include one with each shipment. It should state the way to financial freedom and working for yourself

Target Market(s)

Young Entrepreneurs that want to start and don't know how

Industry/Entity Type

Business

Contact Information for Business Card

"You just bought from a successful company on Brindlemart. I have a unique business model, discovered by me, unlike any other that can make anyone successful. Follow me and message me for exactly the same model. If you ever wanted to work for yourself, I will teach you how. It's not a pipe dream, allow me to guide you out of the box."

Colors
85abd2

Requirements
Must have
• website www.dorianwelkby.example
social @thedorianwelkby

```html
<!DOCTYPE html>
<html lang="en">
<head>
<meta charset="utf-8">
<title>Dorian Welkby – Business Guidance Card</title>
<link rel="stylesheet" href="https://fonts.googleapis.com/css2?family=Arvo:ital,wght@0,400;1,700&family=Rubik:ital,wght@1,400&display=swap">
<style>
  :root {
    --backdrop: #414141;
    --pink-deep: #ff3a68;
    --pink-mid: #ff7d98;
    --pink-soft: #ffb2c1;
    --pink-pale: #ffc4cf;
    --text-light: #ffffff;
    --text-shadow: rgba(120, 20, 45, 0.55);
    --accent-crimson: #d01846;
    --text-dark: #151515;
  }

  html, body {
    margin: 0;
    padding: 0;
    width: 1200px;
    height: 900px;
    overflow: hidden;
    background: var(--backdrop);
  }

  .canvas {
    position: relative;
    width: 1200px;
    height: 900px;
  }

  .card {
    position: absolute;
    left: 431px;
    top: 199px;
    width: 309px;
    height: 500px;
    border-radius: 72px 0 68px 0;
    overflow: hidden;
    background:
      radial-gradient(ellipse 160px 120px at 92% 4%, var(--pink-deep) 0%, rgba(255, 58, 104, 0) 100%),
      radial-gradient(ellipse 180px 200px at 20% 40%, rgba(255, 80, 120, 0.75) 0%, rgba(255, 80, 120, 0) 100%),
      radial-gradient(ellipse 140px 160px at 95% 70%, rgba(255, 95, 130, 0.7) 0%, rgba(255, 95, 130, 0) 100%),
      radial-gradient(ellipse 200px 140px at 30% 95%, var(--pink-pale) 0%, rgba(255, 196, 207, 0) 100%),
      linear-gradient(170deg, var(--pink-mid) 0%, var(--pink-mid) 40%, var(--pink-soft) 75%, var(--pink-pale) 100%);
    text-align: center;
  }

  .card__pitch {
    position: absolute;
    left: 0;
    right: 0;
    top: 38px;
    margin: 0;
    font-family: "Arvo", "Rockwell", serif;
    font-style: italic;
    font-weight: 700;
    font-size: 17.5px;
    line-height: 26.3px;
    color: var(--text-light);
    text-shadow: 1px 1px 1px var(--text-shadow);
  }

  .card__cta {
    position: absolute;
    left: 0;
    right: 0;
    top: 410px;
    margin: 0;
    font-family: "Rubik", "Helvetica", sans-serif;
    font-style: italic;
    font-weight: 400;
    font-size: 16.5px;
    color: var(--accent-crimson);
  }

  .card__contact {
    position: absolute;
    left: 0;
    right: 0;
    top: 437px;
    margin: 0;
    font-family: "Arvo", "Rockwell", serif;
    font-weight: 400;
    font-size: 15px;
    line-height: 20.5px;
    color: var(--text-dark);
  }
</style>
</head>
<body>
  <main class="canvas">
    <article class="card">
      <p class="card__pitch">
        You just bought from a<br>
        successful company on<br>
        Brindlemart. I have a unique<br>
        business model, discovered<br>
        by me, unlike any other that<br>
        can make anyone success-<br>
        ful.&nbsp; Follow me and message<br>
        me for exactly the same<br>
        model. If you ever wanted to<br>
        work for yourself, I will<br>
        teach you how. It's not a<br>
        pipe dream, allow me to<br>
        guide you out of the box
      </p>
      <p class="card__cta">For More Details</p>
      <p class="card__contact">
        <span class="card__website">www.dorianwelkby.example</span><br>
        <span class="card__social">social: @thedorianwelkby</span>
      </p>
    </article>
  </main>
</body>
</html>
```